Postcard Design

we need an A5 size(B: Flyer design) postcard to promote Velira Fashion, we are an evening wear company based in london se17 4qd.we specialize in party dresses, prom & evening wear. we would like to have 2 or 3 dresses featured on the card.Also note that we will be exhibiting at Malmo (Sweden) Coastway Wedding Fair on 1st & 2nd of August 2015 . The card should feature 10% off all purchases at the Malmo exhibition. For the reverse side we need normal standard postcard which we can send to our customers. The stand number will be available next week.Could you please combine 2-4 images so the card looks presentable.Nordic Bridal Show1st-2nd August 2015Stand

```html
<!DOCTYPE html>
<html lang="en">
<head>
<meta charset="utf-8">
<title>Velira Fashion – Postcard</title>
<link rel="stylesheet" href="https://fonts.googleapis.com/css2?family=Great+Vibes&family=Montserrat:wght@400;600;700;800&display=swap">
<style>
  :root {
    --canvas: #e6e4e1;
    --card-dark: #0b0b0b;
    --card-light: #ffffff;
    --pink: #e0245e;
    --green: #8dc63f;
    --white: #ffffff;
    --ink: #111111;
    --stamp: #9a9a9a;
  }
  html, body {
    margin: 0;
    padding: 0;
    width: 900px;
    height: 1200px;
    overflow: hidden;
    background: var(--canvas);
  }
  .postcard {
    position: absolute;
    left: 40px;
    width: 820px;
    height: 547px;
    box-shadow: 0 6px 18px rgba(0,0,0,0.25);
  }
  .postcard--front { top: 40px; }
  .postcard--back  { top: 613px; }
  .postcard svg { display: block; width: 820px; height: 547px; }

  .script { font-family: 'Great Vibes', cursive; }
  .sans { font-family: 'Montserrat', Arial, sans-serif; }

  .headline { fill: var(--green); font-size: 44px; }
  .headline-sub { fill: var(--pink); font-size: 28px; }
  .event-line { fill: var(--white); font-size: 22px; font-weight: 600; }
  .event-date { fill: var(--white); font-size: 24px; font-weight: 700; }
  .event-date tspan.sup { font-size: 13px; }
  .offer-big { fill: var(--pink); font-size: 44px; font-weight: 800; }
  .offer-small { fill: var(--pink); font-size: 16px; font-weight: 800; }
  .offer-text { fill: var(--ink); font-size: 16px; font-weight: 700; }
  .brand-name--front { fill: var(--white); font-size: 34px; font-weight: 700; }
  .brand-name--back { fill: var(--ink); font-size: 32px; font-weight: 700; }
  .specialize-title { fill: var(--white); font-size: 18px; font-weight: 700; letter-spacing: 1px; }
  .specialize-item { fill: var(--white); font-size: 13px; font-weight: 400; }
  .website { fill: var(--white); font-size: 15px; font-weight: 700; letter-spacing: 0.5px; }
</style>
</head>
<body>

<section class="postcard postcard--front">
  <svg viewBox="0 0 820 547" xmlns="http://www.w3.org/2000/svg">
    <defs>
      <linearGradient id="gown-main" x1="0" y1="0" x2="1" y2="1">
        <stop offset="0" stop-color="#dcd9d3"/>
        <stop offset="0.5" stop-color="#ece4d6"/>
        <stop offset="1" stop-color="#a9a59d"/>
      </linearGradient>
      <linearGradient id="gown-ivory" x1="0" y1="0" x2="0" y2="1">
        <stop offset="0" stop-color="#d6d0c6"/>
        <stop offset="1" stop-color="#8d877e"/>
      </linearGradient>
      <linearGradient id="gown-navy" x1="0" y1="0" x2="0" y2="1">
        <stop offset="0" stop-color="#8a93a8"/>
        <stop offset="1" stop-color="#2f3a58"/>
      </linearGradient>
    </defs>

    <rect class="card-base" width="820" height="547" fill="var(--card-dark)"/>

    <path role="img" aria-label="Photo of a model in a long ivory evening gown" d="M0,0 H300 C380,120 380,400 300,547 H0 Z" fill="url(#gown-main)"/>
    <path class="edge-curve edge-curve--pink" d="M312,0 C394,120 394,400 312,547" fill="none" stroke="var(--pink)" stroke-width="10"/>
    <path class="edge-curve edge-curve--green" d="M328,0 C410,130 410,390 328,547" fill="none" stroke="var(--green)" stroke-width="5"/>

    <path class="swoosh swoosh--top" d="M470,0 H820 V80 C730,25 620,8 470,0 Z" fill="var(--pink)"/>
    <path class="swoosh swoosh--top-line" d="M470,0 C620,14 730,36 820,96" fill="none" stroke="var(--green)" stroke-width="4"/>
    <path class="swoosh swoosh--bottom" d="M820,547 H540 C650,530 760,500 820,450 Z" fill="#1e1e1e"/>

    <circle cx="402" cy="248" r="66" fill="none" stroke="var(--pink)" stroke-width="5"/>
    <circle role="img" aria-label="Photo of an ivory gown" cx="402" cy="248" r="56" fill="url(#gown-ivory)" stroke="var(--green)" stroke-width="8"/>
    <circle cx="362" cy="402" r="58" fill="none" stroke="var(--green)" stroke-width="5"/>
    <circle role="img" aria-label="Photo of a navy evening dress" cx="362" cy="402" r="48" fill="url(#gown-navy)" stroke="var(--pink)" stroke-width="7"/>

    <text class="script headline" x="485" y="115">Exhibiting at Malmo</text>
    <text class="script headline-sub" x="610" y="145">(Sweden)</text>
    <text class="sans event-line" x="470" y="200">Coastway Wedding Fair on</text>
    <text class="sans event-date" x="470" y="238">1<tspan class="sup" dy="-9">st</tspan><tspan dy="9"> &amp; 2</tspan><tspan class="sup" dy="-9">nd</tspan><tspan dy="9"> of August 2015</tspan></text>

    <rect class="offer-band" x="455" y="298" width="365" height="74" fill="var(--green)"/>
    <text class="sans offer-big" x="468" y="346">10%</text>
    <text class="sans offer-small" x="470" y="366">OFF</text>
    <text class="sans offer-text" x="585" y="322">ALL PURCHASES</text>
    <text class="sans offer-text" x="585" y="342">AT THE MALMO</text>
    <text class="sans offer-text" x="585" y="362">EXHIBITION</text>

    <text class="sans brand-name--front" x="470" y="448">Velira Fashion</text>
  </svg>
</section>

<section class="postcard postcard--back">
  <svg viewBox="0 0 820 547" xmlns="http://www.w3.org/2000/svg">
    <defs>
      <linearGradient id="gown-back" x1="0" y1="0" x2="1" y2="1">
        <stop offset="0" stop-color="#c9d3d8"/>
        <stop offset="0.5" stop-color="#ece3d4"/>
        <stop offset="1" stop-color="#a7a196"/>
      </linearGradient>
    </defs>

    <rect class="card-base" width="820" height="547" fill="var(--card-light)"/>

    <path class="promo-panel" d="M0,0 H300 C372,150 362,400 290,547 H0 Z" fill="var(--card-dark)"/>
    <path class="edge-curve edge-curve--pink" d="M304,0 C378,150 368,400 296,547" fill="none" stroke="var(--pink)" stroke-width="8"/>
    <path class="edge-curve edge-curve--green" d="M318,0 C392,150 382,400 310,547" fill="none" stroke="var(--green)" stroke-width="4"/>

    <path role="img" aria-label="Photo of a model in a pale evening gown" d="M22,22 H252 C292,100 292,210 250,292 H22 Z" fill="url(#gown-back)"/>
    <path d="M262,22 C302,100 302,210 260,292" fill="none" stroke="var(--green)" stroke-width="4"/>

    <path class="specialize-band" d="M0,318 H312 L296,358 H0 Z" fill="var(--pink)"/>
    <text class="sans specialize-title" x="22" y="345">SPECIALIZE IN</text>

    <circle cx="30" cy="386" r="3.5" fill="var(--pink)"/>
    <text class="sans specialize-item" x="40" y="390">Party Dresses</text>
    <circle cx="30" cy="410" r="3.5" fill="var(--pink)"/>
    <text class="sans specialize-item" x="40" y="414">Prom Dresses</text>
    <circle cx="160" cy="386" r="3.5" fill="var(--pink)"/>
    <text class="sans specialize-item" x="170" y="390">Evening Wear</text>
    <circle cx="160" cy="410" r="3.5" fill="var(--pink)"/>
    <text class="sans specialize-item" x="170" y="414">Bridal Wear</text>

    <text class="sans website" x="22" y="495">WWW.VELIRAFASHION.COM</text>

    <text class="sans brand-name--back" x="430" y="100">Velira</text>
    <g class="stamp-box">
      <rect x="690" y="40" width="92" height="108" fill="none" stroke="var(--stamp)" stroke-width="2" stroke-dasharray="5 4"/>
      <rect x="700" y="50" width="72" height="88" fill="none" stroke="var(--stamp)" stroke-width="1"/>
    </g>
  </svg>
</section>

</body>
</html>
```